10-slide template for ESG report for small businesses in Europe

Presentation goal: for owners of small businesses in Europe to report on their ESG metrics to various internal and external stakeholders, but typically used as part of their annual (financial) report.
Who is the target audience: small business owners/managers in Europe (these are business people, but not very corporate)
How is it going to be used: this template will be used to generate PDF reports automatically based on various inputs. The final output will not be reviewed or corrected by a human; hence we need to make sure that the template is flexible enough to be used for a variety of different inputs (specifically, in some cases there will be no input, and in some cases there will be many characters).
Desired look and feel: following VelloQuist brand style guide (attached). It's for business use so it's somewhat formal, but I do not want it to come across too corporate, so it's OK if there are playful elements.
What is the catch: the fact the template will need to be flexible enough to allow for the report to still look OK even if a certain fields do not have a value (specifically, as mentioned earlier there are some text fields that are likely going to be empty, but could have up to 1000 characters of text).
Illustrations: to keep it generic and relevant for a variety of businesses across all of Europe it's probably better to use simple flat style illustrations instead of photos. I've been using https://brindlecove.example/ to create those (see example attached) but I'm open to anything.
Lastly: please note that I'm very open to changing the position and size of all copy, tables, illustrations etc. I know I'm a terrible designer - that's why I'm here ;-)
Look and feel
Each slider illustrates characteristics of the customer's brand and the style your logo design should communicate.

```html
<!DOCTYPE html>
<html lang="en">
<head>
<meta charset="utf-8">
<title>ESG Report Template – VelloQuist</title>
<link href="https://fonts.googleapis.com/css2?family=Lato:wght@300;400;700;900&display=swap" rel="stylesheet">
<style>
  :root {
    --page: #fdfdf8;
    --slide: #fcfdf5;
    --ink: #23242e;
    --body: #7a7d85;
    --muted: #9a9ca3;
    --accent: #4a5ae8;
    --lime: #a8cc1f;
    --navy: #1d2b52;
  }
  * { margin: 0; padding: 0; box-sizing: border-box; }
  html, body { width: 1061px; height: 1200px; overflow: hidden; background: var(--page); }
  body { position: relative; font-family: "Lato", sans-serif; color: var(--ink); }

  .slide {
    position: absolute; left: 0; width: 999px; overflow: hidden;
    background: var(--slide);
    box-shadow: 0 18px 40px rgba(120, 125, 90, 0.10);
  }
  .slide--cover { top: 0; height: 584px; }
  .slide--intro { top: 608px; height: 528px; }

  .brand { position: absolute; left: 60px; display: flex; align-items: center; }
  .brand__rule { width: 38px; height: 1px; background: var(--lime); margin-right: 10px; }
  .brand__mark { width: 9px; height: 9px; background: var(--navy); margin-right: 4px; }
  .brand__name { font-size: 14px; font-weight: 700; color: var(--navy); letter-spacing: 0.1px; }

  .social {
    position: absolute; left: 78px; writing-mode: vertical-rl; transform: rotate(180deg);
    font-size: 9px; color: var(--muted); letter-spacing: 0.5px; word-spacing: 14px;
  }

  .footer { position: absolute; left: 81px; display: flex; align-items: center; font-size: 10px; }
  .footer__num { font-weight: 700; color: var(--ink); width: 16px; }
  .footer__rule { width: 43px; height: 1px; background: var(--muted); margin-right: 16px; }
  .footer__text { color: var(--muted); font-weight: 300; }

  .placeholder { color: var(--accent); font-weight: 300; }
  .accent-bar { position: absolute; height: 4px; background: var(--accent); }

  .cover__period { position: absolute; left: 166px; top: 186px; font-size: 20px; }
  .cover__title {
    position: absolute; left: 166px; top: 270px; font-size: 36px; font-weight: 900;
    line-height: 51px; letter-spacing: -0.2px;
  }
  .cover__business { position: absolute; left: 166px; top: 405px; font-size: 20px; }

  .illustration {
    position: absolute; border-radius: 40% 48% 12% 30%;
    background:
      radial-gradient(circle at 18% 65%, rgba(240,124,117,.55), transparent 40%),
      radial-gradient(circle at 45% 60%, rgba(248,193,60,.55), transparent 42%),
      radial-gradient(circle at 78% 60%, rgba(91,196,220,.55), transparent 42%),
      radial-gradient(circle at 45% 30%, rgba(74,111,181,.45), transparent 40%),
      linear-gradient(160deg, #f6f4e8, #eef3ec);
  }
  .illustration--cover { left: 603px; top: 180px; width: 290px; height: 275px; }
  .illustration--intro { left: 710px; top: 256px; width: 289px; height: 272px; }

  .intro__title { position: absolute; left: 108px; top: 76px; font-size: 22px; font-weight: 700; }
  .intro__body {
    position: absolute; left: 108px; top: 118px; width: 584px;
    font-size: 11.3px; font-weight: 300; color: var(--body); line-height: 21.2px;
  }
  .intro__body p + p { margin-top: 21.2px; }
  .intro__sign { position: absolute; left: 108px; top: 462px; display: flex; gap: 37px; font-size: 11.5px; }
  .intro__sign .placeholder { font-weight: 400; }
</style>
</head>
<body>

<section class="slide slide--cover">
  <div class="brand" style="top:89px;">
    <span class="brand__rule"></span><span class="brand__mark"></span><span class="brand__name">VelloQuist</span>
  </div>
  <div class="cover__period placeholder">[reporting period]</div>
  <div class="accent-bar" style="left:166px; top:251px; width:40px;"></div>
  <h1 class="cover__title">Environmental, Social,<br>and Governance Report</h1>
  <div class="cover__business placeholder">[business name]</div>
  <div class="illustration illustration--cover" role="img" aria-label="Flat illustration of three colleagues collaborating around a desk with laptops, plants and idea icons"></div>
  <div class="social" style="top:452px;">Fb Tw Ln</div>
  <div class="footer" style="top:554px;">
    <span class="footer__num">1</span><span class="footer__rule"></span>
    <span class="footer__text">[reporting period] Environmental, Social, and Governance Report | [business name]</span>
  </div>
</section>

<section class="slide slide--intro">
  <div class="brand" style="top:34px;">
    <span class="brand__rule"></span><span class="brand__mark"></span><span class="brand__name">VelloQuist</span>
  </div>
  <div class="accent-bar" style="left:108px; top:66px; width:38px; height:3px;"></div>
  <h2 class="intro__title">Introduction</h2>
  <div class="intro__body">
    <p>Dear reader,</p>
    <p>We are pleased to present our annual ESG report, outlining our commitment and progress on key environmental, social and governance priorities. As a responsible business, we understand our obligation to consider our environmental and social impacts.</p>
    <p>This annual ESG report summarises our commitment to sustainability across our operations. Through data-driven insights, we have focused our strategy on material issues from carbon emissions to ethical conduct. While progress has been made, opportunities to improve remain.</p>
    <p>We will continue to embed responsible practices through collaboration with our stakeholders. Our aim is to drive long-term value creation by upholding the highest standards of integrity, championing diversity and inclusion, and supporting climate action. Though the road ahead is long, we are confident our collective efforts will build a resilient, equitable and sustainable future.</p>
  </div>
  <div class="intro__sign">
    <span class="placeholder">[full name]</span><span class="placeholder">[business name]</span>
  </div>
  <div class="illustration illustration--intro" role="img" aria-label="Flat illustration of three colleagues collaborating around a desk with laptops, plants and idea icons"></div>
  <div class="social" style="top:396px;">Fb Tw Ln</div>
  <div class="footer" style="top:498px;">
    <span class="footer__num">2</span><span class="footer__rule"></span>
    <span class="footer__text">[reporting period] Environmental, Social, and Governance Report | [business name]</span>
  </div>
</section>

</body>
</html>
```